Ductless Mini Split Business Website

Amber Kite Services is looking to design an eye catching educational website about installing Ductless mini splits.

Similar to this company.
https://www.cedarcoolair.com/

```html
<!DOCTYPE html>
<html lang="en">
<head>
<meta charset="utf-8">
<title>Amber Kite Services – Ductless Experts</title>
<link href="https://fonts.googleapis.com/css2?family=Poppins:ital,wght@0,300;0,400;0,500;0,600;1,300;1,400&display=swap" rel="stylesheet">
<style>
:root{
  --yellow:#fbd20d;
  --yellow-soft:#fdf7c2;
  --yellow-bar:#fcf8c6;
  --ink:#2b2b2b;
  --text:#3a3a3a;
  --muted:#8a8a8a;
  --line:#e6e6e6;
  --dark-band:rgba(30,30,30,.82);
  --white:#ffffff;
}
*{box-sizing:border-box;margin:0;padding:0}
html,body{width:1200px;height:4637px;overflow:hidden}
body{position:relative;background:var(--white);font-family:"Poppins",sans-serif;color:var(--text)}
.abs{position:absolute}
.blobs{position:absolute;left:0;top:0;z-index:0}
.layer{position:relative;z-index:1}

.topbar{left:0;top:0;width:1200px;height:50px;background:var(--yellow-bar)}
.topbar p{position:absolute;right:48px;top:14px;font-size:14px;color:var(--ink)}
.topbar strong{font-size:19px;font-weight:600}

.brand{left:38px;top:74px;display:flex;align-items:center;gap:10px}
.brand-dot{width:34px;height:34px;border-radius:50%;background:var(--yellow)}
.brand-name{font-size:16px;font-weight:600;color:var(--ink);line-height:1.2;width:130px}

.nav{top:94px;left:0;width:1200px;font-size:14.5px;color:var(--ink)}
.nav a{position:absolute;text-decoration:none;color:inherit;white-space:nowrap}
.nav a.active{border-bottom:2px solid var(--yellow);padding-bottom:4px}
.nav .chev{display:inline-block;width:7px;height:7px;border-right:1px solid #777;border-bottom:1px solid #777;transform:rotate(45deg);margin:0 0 3px 6px}

.hero-title{left:108px;top:212px;font-size:60px;font-weight:400;line-height:90px;color:var(--ink)}
.hero-title .hl{color:var(--yellow)}
.hero-sub{left:108px;top:590px;font-size:17px;color:var(--muted)}
.btn{display:flex;align-items:center;justify-content:center;border-radius:30px;font-size:13px;font-weight:500}
.btn-dark{left:108px;top:670px;width:140px;height:45px;background:var(--ink);color:var(--yellow);box-shadow:0 8px 22px rgba(0,0,0,.18)}

.laptop{left:531px;top:293px;width:563px;height:333px}
.laptop-lid{position:absolute;left:44px;top:0;width:476px;height:310px;background:#e9e9e9;border-radius:14px;box-shadow:0 6px 18px rgba(0,0,0,.1)}
.laptop-screen{position:absolute;left:18px;top:18px;width:440px;height:272px;background:linear-gradient(135deg,#f3efe9,#d8d0c4 55%,#b9a898)}
.laptop-base{position:absolute;left:0;top:310px;width:563px;height:12px;background:linear-gradient(#dcdcdc,#bdbdbd);border-radius:0 0 40px 40px}

.about-photo{left:108px;top:806px;width:306px;height:405px;background:linear-gradient(160deg,#c8c2b4,#8e8576 50%,#5a5148)}
.play{left:384px;top:978px;width:60px;height:60px;border-radius:50%;background:var(--yellow);display:flex;align-items:center;justify-content:center}
.about-title{left:529px;top:805px;width:590px;font-size:42px;font-weight:400;line-height:60px;color:var(--ink)}
.about-copy{left:529px;top:946px;width:570px;font-size:13.2px;line-height:28.8px;color:#6a6a6a}
.about-copy p+p{margin-top:14px}

.section-title{left:0;width:1200px;text-align:center;font-size:42px;font-weight:400;color:var(--ink)}

.card{width:238px;height:238px;overflow:hidden}
.card .ph{position:absolute;inset:0}
.card .label{position:absolute;left:0;bottom:0;width:100%;height:54px;background:var(--dark-band);color:var(--yellow);font-size:13.5px;font-weight:500;letter-spacing:.5px;text-align:center;display:flex;align-items:center;justify-content:center;line-height:19px;text-transform:uppercase}
.card-info{background:#eef2f7;box-shadow:0 10px 30px rgba(120,140,170,.18)}
.card-info p{position:absolute;left:27px;top:36px;width:190px;font-size:17px;line-height:25px;color:var(--ink)}
.card-info .ghost{position:absolute;left:0;bottom:12px;width:100%;text-align:center;color:#d8dde4;font-size:13px;font-weight:500;line-height:19px}
.card-info .go{position:absolute;left:148px;top:150px;width:52px;height:52px;border-radius:50%;background:var(--yellow);display:flex;align-items:center;justify-content:center}

.qwg-title{left:121px;top:2122px;font-size:40px;color:var(--ink)}
.qwg-copy{left:121px;top:2188px;width:960px;font-size:13.5px;line-height:22px;color:#7a7a7a}

.avatar{left:207px;top:2372px;width:152px;height:152px;border-radius:50%;background:radial-gradient(circle at 50% 45%,#dfe6ee,#b9c4d0)}
.quote{left:410px;top:2342px;width:560px;font-size:20.5px;font-style:italic;font-weight:300;line-height:29.5px;color:var(--ink)}
.stars{left:410px;top:2490px;color:var(--yellow);font-size:17px;letter-spacing:1px}
.author{left:410px;top:2522px;font-size:17px;color:var(--ink)}
.arrow-l,.arrow-r{top:2436px;width:18px;height:18px;border-left:2px solid #999;border-bottom:2px solid #999}
.arrow-l{left:124px;transform:rotate(45deg)}
.arrow-r{left:1064px;transform:rotate(-135deg)}
.bigquote{left:950px;top:2470px;font-size:110px;color:var(--yellow-soft);font-family:"Poppins",sans-serif;font-weight:600;line-height:1}
.rule{left:112px;width:982px;height:1px;background:var(--line)}

.feature{width:320px;text-align:center}
.feature .blob{margin:0 auto;width:130px;height:94px;border-radius:48% 52% 50% 50% / 60% 55% 45% 40%;background:var(--yellow-soft);display:flex;align-items:center;justify-content:center}
.feature.main .blob{background:var(--yellow);box-shadow:0 12px 26px rgba(251,210,13,.35)}
.feature h3{margin-top:44px;font-size:17.5px;font-weight:400;color:var(--ink)}
.feature.main h3{color:var(--yellow)}
.feature p{margin-top:14px;font-size:12.6px;line-height:28px;color:#8a8a8a;padding:0 10px}

.stand-sub{left:0;top:3215px;width:1200px;text-align:center;font-size:16px;color:var(--ink)}
.tile{top:3303px;width:300px;height:301px}
.tile-blog{background:linear-gradient(160deg,#eef3fa,#dfe8f4);box-shadow:0 10px 28px rgba(120,140,170,.2)}
.tile-blog h4{position:absolute;left:27px;top:38px;font-size:23px;font-weight:400;color:var(--ink)}
.tile-blog span{position:absolute;left:27px;top:82px;font-size:12.5px;color:#8a8a8a}
.btn-yellow{background:var(--yellow);color:var(--white)}
.tile-blog .btn{position:absolute;left:81px;top:129px;width:138px;height:40px;font-size:12px;box-shadow:0 8px 18px rgba(251,210,13,.35)}

.contact-title{left:106px;top:3720px;font-size:29px;color:var(--ink)}
.contact-lines{left:106px;top:3768px;font-size:21px;line-height:29px;color:var(--ink)}
.field{height:45px;border:1px solid #d6d6d6;border-radius:24px;font-size:11.5px;color:#888;padding:13px 18px}
.field-msg{height:97px;border-radius:22px;padding-top:22px}
.btn-send{left:108px;top:4149px;width:140px;height:45px;box-shadow:0 8px 18px rgba(251,210,13,.35)}

.foot h5{font-size:20px;font-weight:400;color:var(--ink);margin-bottom:24px}
.foot li{list-style:none;font-size:13px;color:#7a7a7a;line-height:34px}
.foot .addr{font-size:13px;line-height:28px;color:#7a7a7a}
.foot .phone{margin-top:20px;font-size:25px;color:var(--yellow)}
.foot .about{font-size:13px;line-height:29px;color:#7a7a7a;width:330px}
.socials{display:flex;gap:9px;margin-top:14px}
.socials span{width:33px;height:33px;border-radius:50%}
.copyright{left:94px;top:4592px;font-size:12px;color:#666}
.to-top{left:1110px;top:4546px;width:44px;height:44px;border-radius:50%;background:var(--yellow);display:flex;align-items:center;justify-content:center}
</style>
</head>
<body>

<svg class="blobs" width="1200" height="4637" viewBox="0 0 1200 4637" aria-hidden="true">
  <g fill="#fdf7c2">
    <path d="M365 140 C400 50 680 60 790 170 C900 90 1130 60 1200 120 L1200 560 C1100 640 900 700 700 690 C520 680 400 500 380 360 Z"/>
    <path d="M0 805 C90 860 150 1000 125 1150 C105 1230 45 1260 0 1270 Z"/>
    <path d="M1200 2060 C1050 2080 880 2160 860 2300 C850 2450 1000 2570 1200 2660 Z"/>
    <path d="M0 3060 C160 3110 400 3300 410 3500 C420 3650 300 3700 200 3770 C100 3830 40 3900 0 3950 Z"/>
  </g>
</svg>

<div class="layer">
  <div class="abs topbar"><p>Call Us Today - <strong>(500) 555-0184</strong></p></div>

  <div class="abs brand"><span class="brand-dot"></span><span class="brand-name">Amber Kite Services</span></div>

  <nav class="abs nav">
    <a class="active" style="left:365px">Home</a>
    <a style="left:432px">About<span class="chev"></span></a>
    <a style="left:515px">Ductless Heat Pumps<span class="chev"></span></a>
    <a style="left:707px">Ductless Heat Pumps FAQ</a>
    <a style="left:916px">Financing</a>
    <a style="left:1013px">Reviews</a>
    <a style="left:1096px">Contact</a>
  </nav>

  <h1 class="abs hero-title">We are<br>Experts in<br><span class="hl">Ductless Mini<br>Splits</span></h1>
  <p class="abs hero-sub">AmberKite is Better Ductless Services</p>
  <div class="abs btn btn-dark">Contact Us</div>

  <div class="abs laptop">
    <div class="laptop-lid"><div class="laptop-screen" role="img" aria-label="Family relaxing on a sofa under a wall-mounted mini split"></div></div>
    <div class="laptop-base"></div>
  </div>

  <div class="abs about-photo" role="img" aria-label="Couple by a window in a room with a ductless unit"></div>
  <div class="abs play"><svg width="20" height="20" viewBox="0 0 20 20"><path d="M6 3 L17 10 L6 17 Z" fill="#fff"/></svg></div>
  <h2 class="abs about-title">Amber Kite Services - Ductless Mini Splits Experts</h2>
  <div class="abs about-copy">
    <p>Experience maximum comfort, better indoor air quality, and lower utility bills by installing ductless heat pumps in your home. As the premier company for everything ductless-related, Amber Kite offers a wide selection of quality ductless systems from industry-leading manufacturers. We are also the experts when it comes to unparalleled ductless solutions.</p>
    <p>Whether you need repairs or maintenance for an existing unit or are considering switching your baseboard heating with a ductless heat pump, our trained technicians can do it all. Our technicians are eager for you to enjoy the many benefits of a ductless system!</p>
  </div>

  <h2 class="abs section-title" style="top:1340px">How Can We Help You?</h2>

  <div class="abs card" style="left:58px;top:1454px"><div class="ph" role="img" aria-label="Baseboard heater on a white wall" style="background:linear-gradient(#dfe3e3,#a9adab)"></div><div class="label">Baseboard Heat<br>Replacement</div></div>
  <div class="abs card" style="left:340px;top:1454px"><div class="ph" role="img" aria-label="Renovated room with ladder and teal sofa" style="background:linear-gradient(135deg,#ece9e4,#9fc3c2)"></div><div class="label">Ductless for<br>Additions &amp; Remodels</div></div>
  <div class="abs card card-info" style="left:623px;top:1454px">
    <p>Providing Important Information about Ductless Systems.</p>
    <div class="go"><svg width="20" height="14" viewBox="0 0 20 14"><path d="M1 7 H18 M12 1 L18 7 L12 13" stroke="#fff" stroke-width="2" fill="none"/></svg></div>
    <div class="ghost">DUCTLESS HEAT<br>PUMPS FAQ</div>
  </div>
  <div class="abs card" style="left:905px;top:1454px"><div class="ph" role="img" aria-label="Technician installing an indoor unit" style="background:linear-gradient(135deg,#e9ecef,#b6c3cf)"></div><div class="label">Ductless Installation</div></div>

  <div class="abs card" style="left:58px;top:1741px"><div class="ph" role="img" aria-label="Technician cleaning a wall unit" style="background:linear-gradient(135deg,#e7ebee,#c4c9c9)"></div><div class="label">Ductless Maintenance</div></div>
  <div class="abs card" style="left:340px;top:1741px"><div class="ph" role="img" aria-label="Technician repairing a mini split" style="background:linear-gradient(135deg,#dde1e5,#8d949c)"></div><div class="label">Ductless Repairs</div></div>
  <div class="abs card" style="left:623px;top:1741px"><div class="ph" role="img" aria-label="Living room with blue wall and wall unit" style="background:linear-gradient(#a9bccb,#8fa4b3 70%,#c9c3b8)"></div><div class="label">Ductless Warranty</div></div>
  <div class="abs card" style="left:905px;top:1741px"><div class="ph" role="img" aria-label="Open-plan home with high ceilings" style="background:linear-gradient(135deg,#f0ede8,#b3a08a)"></div><div class="label">Whole House Ductless</div></div>

  <h2 class="abs qwg-title">Quality Work Guarantee</h2>
  <p class="abs qwg-copy">Amber Kite Services, we take great pride in our work. As the only heating and cooling company in the area that specializes in ductless systems, our expert technicians provide only the highest level of service every time. We have the resources and the training as a Norvale 3D Dealer and Kestrel Premier Contractor to get the job done. Trust us to deliver total home comfort with our high-performing, energy-efficient ductless heat pumps or air conditioners and superior workmanship.</p>

  <div class="abs arrow-l"></div>
  <div class="abs arrow-r"></div>
  <div class="abs avatar" role="img" aria-label="Customer portrait"></div>
  <p class="abs quote">"Amber Kite Ductless did FANTASTIC work installing a new ductless heat pump for my customer. Everything was straightforward, great scheduling, and the installers were super knowledgeable about the product."</p>
  <div class="abs stars">★★★★★</div>
  <div class="abs author">- Jordan T</div>
  <div class="abs bigquote">”</div>
  <div class="abs rule" style="top:2615px"></div>

  <h2 class="abs section-title" style="top:2683px">Why Choose Amber Kite Services</h2>

  <div class="abs feature" style="left:101px;top:2797px">
    <div class="blob"><svg width="34" height="34" viewBox="0 0 34 34" fill="none" stroke="#333" stroke-width="1.6"><path d="M12 4 H22 M17 4 V10 M10 24 L17 10 L24 24 Z M7 30 H27"/></svg></div>
    <h3>0% Financing for 60 months</h3>
    <p>Providing options to our customers where it matters most. Offer applies to Halvorn systems.</p>
  </div>
  <div class="abs feature main" style="left:440px;top:2797px">
    <div class="blob"><svg width="38" height="38" viewBox="0 0 38 38" fill="none" stroke="#333" stroke-width="2"><circle cx="19" cy="19" r="14"/><path d="M19 5 V19 L29 29"/><path d="M19 19 L19 5 A14 14 0 0 1 29 29 Z" fill="#333"/></svg></div>
    <h3>365 Day, Money Back Guarantee</h3>
    <p>We have integrity, and stand behind our services to ensure that you are satisfied.</p>
  </div>
  <div class="abs feature" style="left:778px;top:2797px">
    <div class="blob"><svg width="36" height="36" viewBox="0 0 36 36" fill="none" stroke="#333" stroke-width="1.6"><rect x="5" y="5" width="26" height="18"/><path d="M10 18 L15 13 L19 16 L26 9 M18 23 V28 M13 32 L18 28 L23 32"/></svg></div>
    <h3>Experts in Ductless Services</h3>
    <p>Not only can we perform the services with precision, but we can also educate you on why ductless is the way to do.</p>
  </div>

  <h2 class="abs section-title" style="top:3150px">We Stand Behind Our Ductless Services</h2>
  <p class="abs stand-sub">See Other Ways We Can Help with Your Ductless Systems</p>

  <div class="abs tile" style="left:106px" role="img" aria-label="Bright room with lounge chair and ductless unit"><div style="position:absolute;inset:0;background:linear-gradient(160deg,#f4f4f2,#c9d4c4 55%,#5e6b55)"></div></div>
  <div class="abs tile" style="left:450px" role="img" aria-label="Hand holding cash for financing"><div style="position:absolute;inset:0;background:linear-gradient(135deg,#cfd3c4,#8e9484 50%,#5f6659)"></div></div>
  <div class="abs tile tile-blog" style="left:794px">
    <h4>Stay Up To Date</h4>
    <span>Ductless Heat Pump vs Furnace</span>
    <div class="btn btn-yellow">OUR BLOG</div>
  </div>

  <h2 class="abs contact-title">Contact Us</h2>
  <p class="abs contact-lines">Fill Out the Form Below or Call Amber Kite Services at (500) 555-0184<br>Please fill out the form below to inquire about our work in Digital.</p>

  <div class="abs field" style="left:106px;top:3870px;width:481px">Name</div>
  <div class="abs field" style="left:614px;top:3870px;width:480px">Email</div>
  <div class="abs field" style="left:106px;top:3942px;width:481px">Phone</div>
  <div class="abs field" style="left:614px;top:3942px;width:480px">Organization</div>
  <div class="abs field field-msg" style="left:106px;top:4012px;width:988px">Message</div>
  <div class="abs btn btn-yellow btn-send">Contact Us</div>

  <div class="abs rule" style="top:4293px"></div>

  <div class="abs foot" style="left:106px;top:4336px">
    <h5>Location</h5>
    <p class="addr">2280 NW Juniper Park Way,<br>Suite B214<br>Riverton, OR 97031</p>
    <p class="phone">(500) 555-0184</p>
  </div>
  <div class="abs foot" style="left:360px;top:4336px">
    <h5>Amber Kite Services</h5>
    <ul><li>Home</li><li>About</li><li>Ductless Heat Pumps</li><li>Ductless Heat Pumps FAQ</li></ul>
  </div>
  <div class="abs foot" style="left:614px;top:4336px">
    <h5>Quick Link</h5>
    <ul><li>Financing</li><li>Contact Us</li><li>Privacy Policy</li><li>Sitemap</li></ul>
  </div>
  <div class="abs foot" style="left:783px;top:4336px">
    <h5>About Us</h5>
    <p class="about">Experience maximum comfort, better indoor air quality, and lower utility bills by installing ductless heat pumps in your home.</p>
    <div class="socials"><span style="background:#3b5998"></span><span style="background:#d32323"></span><span style="background:#f5c518"></span><span style="background:#e62117"></span></div>
  </div>

  <p class="abs copyright">Copyright ©2019 | All rights reserved</p>
  <div class="abs to-top"><svg width="16" height="10" viewBox="0 0 16 10"><path d="M2 8 L8 2 L14 8" stroke="#fff" stroke-width="2" fill="none"/></svg></div>
</div>
</body>
</html>
```